Pet product line, needs a label design

We are a pharmaceutical company focused on animal health. We have been in the Mexican and Central American market for 10 years. During this time we have developed our line for production animals (beef, poultry, dairy, pigs...) and now we want to develop a line for pets.
Our first product are some pills made of Yucca (Yucca schidigera) which helps the digestive system of cats and dogs improve, reducing gas production and diminishing the bad smell of the pet feces.
We are looking for a design that can represent our new product line using this new product as an example, its name is 'BRONTAVEX'. The brand umbrella is TQ Vira, I am attaching this logo.
We need an attractive and original design with a strong personality, capable of jumping to the eyes of the consumer (pet owner) and also attractive for the Veterinarian who will recommend the product.
We want to highlight the benefits of the product by developing icons to the three main claims of the product.
We hope you will find this project attractive and challenging!!

Target Market(s)

Pet owners (mainly dog and cat)

Veterinarians

Industry/Entity Type

Pharmaceutical

Requirements
Must have
• * Product name (BRONTAVEX)
* Label Information (added in a word document)
* Band umbrella logo TQ Vira
* GREAT DESIGN
* The design should be horizontal (5cm height and 13 cm width)
Nice to have
• Nice product name design

Icon designs for the following claims (in spanish):
+ Limpia el trato digestivo (Cleans the digestive tract)
+ Reduce los malos olores (Reduces odors)
+ Propicia la digestión completa (Promotes complete digestion)

```html
<!DOCTYPE html>
<html lang="es">
<head>
<meta charset="utf-8">
<title>BRONTAVEX – etiqueta</title>
<link rel="stylesheet" href="https://fonts.googleapis.com/css2?family=PT+Serif:ital,wght@0,400;0,700;1,400&family=Varela+Round&display=swap">
<style>
  :root {
    --bg: #b9b3c8;
    --bg-light: #dcd8e4;
    --label: #ffffff;
    --ink: #3b3b3b;
    --lavender: #b2a4d2;
    --lavender-deep: #9c8cc3;
    --band: #c3b6dc;
    --heart: #f1c9d6;
    --heart-soft: #f9e6ec;
    --logo-green: #6fae8f;
    --rule: #8a8a8a;
  }
  * { box-sizing: border-box; margin: 0; padding: 0; }
  html, body { width: 1200px; height: 900px; overflow: hidden; }
  body {
    background: radial-gradient(ellipse at 50% 35%, var(--bg-light), var(--bg) 75%);
    font-family: "PT Serif", Georgia, serif;
    color: var(--ink);
    position: relative;
  }
  .label {
    position: absolute;
    left: 60px; top: 200px;
    width: 1080px; height: 500px;
    background: var(--label);
    display: grid;
    grid-template-columns: repeat(3, 1fr);
    box-shadow: 0 10px 30px rgba(60, 50, 90, .18);
    overflow: hidden;
  }
  .panel { position: relative; padding: 34px 34px 0; z-index: 1; }
  .band {
    position: absolute; left: 0; bottom: 0; width: 1080px; height: 46px; z-index: 0;
  }
  .tint {
    position: absolute; inset: 0; z-index: 0;
    background: linear-gradient(160deg, rgba(207,233,228,.35), rgba(255,255,255,0) 40%, rgba(241,201,214,.25) 75%, rgba(195,182,220,.3));
  }
  h2 { font-size: 17px; font-weight: 700; margin-bottom: 4px; line-height: 1.3; }
  p, li { font-size: 15px; line-height: 1.35; }
  ul { list-style: none; padding-left: 22px; }
  ul li::before { content: "- "; }
  .section { margin-bottom: 16px; }

  /* panel: ingredients */
  .analysis {
    border-collapse: collapse; font-size: 13.5px; line-height: 1.3; margin-top: 4px; width: 100%;
  }
  .analysis td { border: 1px solid var(--rule); padding: 1px 6px; }
  .analysis td:last-child { white-space: nowrap; width: 42%; }
  .maker { text-align: center; font-size: 13px; line-height: 1.35; margin-top: 20px; }
  .maker strong { display: block; margin-bottom: 2px; }

  /* panel: front */
  .front { padding-top: 24px; }
  .brand {
    display: flex; align-items: center; gap: 10px; justify-content: flex-end;
  }
  .brand-mark { width: 22px; height: 22px; background: var(--logo-green); }
  .brand-name { font-size: 30px; font-weight: 700; color: var(--logo-green); }
  .heart-art {
    position: absolute; left: 50%; top: 100px; width: 240px; height: 230px;
    transform: translateX(-50%);
    border-radius: 50%;
    background: radial-gradient(closest-side, var(--heart-soft), rgba(241,201,214,.6) 85%, rgba(241,201,214,0) 100%);
  }
  .product-name {
    position: absolute; left: 0; right: 0; top: 186px; text-align: center;
    font-family: "Varela Round", "Nunito", sans-serif; font-size: 46px; color: var(--lavender);
  }
  .content-tab {
    position: absolute; left: 50%; bottom: 22px; transform: translateX(-50%);
    width: 118px; padding: 4px 0 8px; border-radius: 8px 8px 0 0;
    background: var(--lavender-deep); color: #fff; text-align: center;
    font-family: "Varela Round", sans-serif; font-size: 13px; line-height: 1.25;
  }

  /* panel: back */
  .effects p { padding-left: 14px; }
</style>
</head>
<body>
  <div class="label">
    <div class="tint"></div>
    <svg class="band" viewBox="0 0 1080 46" preserveAspectRatio="none" aria-hidden="true">
      <path d="M0 24 C 260 6, 520 38, 780 18 S 1020 10, 1080 22 L1080 46 L0 46 Z" fill="var(--band)"/>
    </svg>

    <section class="panel ingredients">
      <div class="section">
        <h2>Ingredientes Activos</h2>
        <ul><li>Saponinas</li><li>Glicocomponentes</li></ul>
      </div>
      <h2>Análisis bromatológico</h2>
      <table class="analysis">
        <tr><td>Humedad</td><td>Max. 8.2 %</td></tr>
        <tr><td>Proteína Cruda</td><td>Max. 2.0 %</td></tr>
        <tr><td>Grasa Cruda</td><td>Max. 0.5 %</td></tr>
        <tr><td>Fibra Cruda</td><td>Max. 30.0 %</td></tr>
        <tr><td>Cenizas</td><td>Max. 11.0 %</td></tr>
        <tr><td>Carbohidratos</td><td>Max. 42.5 %</td></tr>
        <tr><td colspan="2">Excipiente c.b.p.</td></tr>
      </table>
      <div class="maker">
        <strong>Elaborado para :</strong>
        Norvel Internacional, S.A. de C.V.<br>
        Av. Las Palmas 742<br>
        Colonia Arboleda CP 44120<br>
        Zapopan, Jal.
      </div>
    </section>

    <section class="panel front">
      <div class="brand">
        <span class="brand-mark"></span>
        <span class="brand-name">TQ Vira</span>
      </div>
      <div class="heart-art" role="img" aria-label="Corazón rosa formado por las siluetas de un gato y un perro"></div>
      <div class="product-name">Brontavex</div>
      <div class="content-tab">Contenido<br>60 tabletas</div>
    </section>

    <section class="panel details">
      <div class="section">
        <h2>Contenido</h2>
        <p><em>Yucca schidigera</em> extracto pulverizado</p>
      </div>
      <div class="section">
        <h2>Apariencia</h2>
        <p>Tabletas color café</p>
      </div>
      <div class="section">
        <h2>Dosis</h2>
        <p>Mascotas pequeñas : 1 tableta al día</p>
        <p>Mascotas grandes &nbsp;: 2 tabletas al día</p>
      </div>
      <div class="section effects">
        <h2>Efectos benéficos en mascotas</h2>
        <p>Reduce significativamente los malos olores en los desechos de las mascotas</p>
        <ul>
          <li>Reduce el estrés</li>
          <li>Limpia el tracto digestivo</li>
          <li>Propicia una digestión completa</li>
          <li>Efectos anti-inflamatorios</li>
          <li>Efectos antireumáticos</li>
        </ul>
      </div>
    </section>
  </div>
</body>
</html>
```